Banner Ad Design for Resume Builder Needed

For the ad copy and design of the ad, I leave that up to you. Keep in mind this is a do-it-yourself online resume builder. The site is simple to use and geared towards people who are unsure of how to write/create their own resume.

You can view the site (which isn't finished) and how it works at http://careerforge.demo.tlvworks.net/

I do not want the same color scheme or the logo used in the ad, just the most appealing ad for those looking to use a product like this

I need the ad in these sizes:

300x250, 728x90, 160x600, 468x60, 120x600, 300x100

```html
<!DOCTYPE html>
<html lang="en">
<head>
<meta charset="UTF-8">
<title>Build Your Own Resume – Banner</title>
<link rel="stylesheet" href="https://fonts.googleapis.com/css2?family=Roboto:wght@700;900&display=swap">
<style>
  :root {
    --sky: #8dd3ea;
    --sky-edge: #6fc3df;
    --headline: #f4f8fa;
    --accent-red: #e8453c;
    --star-yellow: #f7e51e;
    --rule-white: #ffffff;
    --corner-dark: #3c3c3e;
    --corner-dark-soft: #48484a;
  }
  html, body {
    margin: 0;
    padding: 0;
    overflow: hidden;
    background: #ffffff;
  }
  .banner {
    position: relative;
    width: 1200px;
    height: 150px;
    overflow: hidden;
    background: var(--sky);
    box-shadow: inset 0 0 0 3px var(--sky-edge);
    font-family: "Roboto", Arial, sans-serif;
  }
  .hand-art {
    position: absolute;
    top: 0;
    width: 200px;
    height: 150px;
    background: linear-gradient(180deg, var(--corner-dark) 0%, var(--corner-dark-soft) 100%);
  }
  .hand-art--left { left: 0; }
  .hand-art--right { right: 0; }
  .headline {
    position: absolute;
    left: 0;
    right: 0;
    margin: 0;
    text-align: center;
    text-transform: uppercase;
    line-height: 1;
    white-space: nowrap;
  }
  .headline__lead {
    top: 10px;
    font-weight: 700;
    font-size: 58px;
    letter-spacing: 1.5px;
    color: var(--headline);
  }
  .headline__product {
    top: 56px;
    font-weight: 700;
    font-size: 82px;
    letter-spacing: 0;
    color: var(--accent-red);
  }
  .flourish {
    position: absolute;
    left: 0;
    top: 0;
    width: 1200px;
    height: 150px;
    pointer-events: none;
  }
</style>
</head>
<body>
  <div class="banner">
    <div class="hand-art hand-art--left" role="img" aria-label="Illustration area: a hand in a red sleeve holding a resume sheet"></div>
    <div class="hand-art hand-art--right" role="img" aria-label="Illustration area: a hand in a red sleeve holding a resume sheet"></div>

    <svg class="flourish" viewBox="0 0 1200 150" aria-hidden="true">
      <line x1="352" y1="101" x2="445" y2="101" stroke="var(--rule-white)" stroke-width="3"/>
      <line x1="752" y1="101" x2="848" y2="101" stroke="var(--rule-white)" stroke-width="3"/>
      <polygon fill="var(--star-yellow)" points="352,85 356.7,96 368,96.5 359,103.5 362.5,115 352,108 341.5,115 345,103.5 336,96.5 347.3,96"/>
      <polygon fill="var(--star-yellow)" points="848,85 852.7,96 864,96.5 855,103.5 858.5,115 848,108 837.5,115 841,103.5 832,96.5 843.3,96"/>
    </svg>

    <p class="headline headline__lead">Build your own</p>
    <p class="headline headline__product">Resume</p>
  </div>
</body>
</html>
```